Business Card Design Project

Construction

Industry/Entity Type

Business

Contact Information for Business Card

I've had the same logo for about 5 years. The logo itself is fine, however I'm looking to get a new design on the card. The green for the log is fine but the grey for the rest of the card is kind of dark and blah. Would like a new look. I'll send the file with the logo.

```html
<!DOCTYPE html>
<html lang="en">
<head>
<meta charset="utf-8">
<title>Clearline Commercial Builders – Business Card</title>
<link href="https://fonts.googleapis.com/css2?family=Roboto:ital,wght@0,400;0,500;0,700;0,900;1,400&display=swap" rel="stylesheet">
<style>
  :root{
    --bg:#3a3b3d;
    --card-dark:#2f3033;
    --card-dark-2:#38393c;
    --silver-1:#f4f4f4;
    --silver-2:#c9caca;
    --green:#3fae49;
    --green-light:#7fd68a;
    --green-dark:#1f7a2b;
    --ink:#1d1d1d;
    --white:#ffffff;
    --muted:#e6e6e6;
  }
  *{box-sizing:border-box;margin:0;padding:0}
  html,body{width:799px;height:1200px;overflow:hidden}
  body{background:var(--bg);font-family:"Roboto",Arial,sans-serif;position:relative}
  .card{position:absolute;left:50px;width:700px;height:400px;border-radius:24px;overflow:hidden;box-shadow:0 14px 30px rgba(0,0,0,.45)}
  .card--front{top:120px}
  .card--back{top:680px}
  .card-bg{position:absolute;inset:0;width:100%;height:100%}
  .abs{position:absolute}

  /* front */
  .logo-mark{left:34px;top:24px;display:flex;align-items:center;gap:10px}
  .logo-mark .square{width:26px;height:26px;background:var(--green)}
  .logo-mark .name{font-weight:900;font-size:20px;color:var(--green);letter-spacing:.5px}
  .title{right:40px;top:18px;text-align:right;color:var(--white)}
  .title .main{font-weight:900;font-size:50px;line-height:1;letter-spacing:.5px}
  .title .sub{font-weight:900;font-size:22px;letter-spacing:1px;margin-top:2px}
  .licenses{left:34px;top:112px;color:var(--ink);font-size:17px;line-height:1.5}
  .licenses b{font-weight:700}
  .naics{left:34px;top:222px;color:var(--white);font-size:17px;line-height:1.3;width:430px}
  .naics b{font-weight:700}
  .lbi{left:26px;top:337px;color:var(--white);font-size:15px;letter-spacing:1px}
  .license-tab{right:0;top:188px;width:250px;height:34px;display:flex;align-items:center;justify-content:center;color:var(--white);font-weight:700;font-size:16px;letter-spacing:.5px}
  .seal{width:96px;height:96px}
  .seal--one{left:450px;top:262px}
  .seal--two{left:565px;top:270px}

  /* back */
  .back-logo{left:40px;top:110px;display:flex;align-items:center;gap:10px}
  .back-logo .square{width:34px;height:34px;background:var(--green)}
  .back-logo .name{font-weight:900;font-size:34px;color:var(--ink);line-height:1}
  .back-sub{left:84px;top:150px;font-weight:900;font-size:15px;letter-spacing:1px;color:var(--ink)}
  .serving{left:30px;top:252px;width:310px;height:34px;display:flex;align-items:center;padding-left:14px;color:var(--white);font-size:16px}
  .person{left:400px;top:66px;color:var(--white)}
  .person .name{color:var(--green-light);font-size:30px;font-weight:500}
  .person .role{font-size:15px;margin-top:2px}
  .contacts{left:400px;top:160px;color:var(--white);font-size:16px;list-style:none}
  .contacts li{display:flex;align-items:center;gap:12px;height:28px}
  .contacts svg{width:16px;height:16px;fill:var(--green-light)}
  .contacts .license{padding-left:28px}
  .years{left:470px;top:318px;width:190px;height:56px}
  .years .ribbon{position:absolute;left:0;top:10px;width:190px;height:30px;background:var(--green);display:flex;align-items:center;justify-content:center;color:var(--white);font-weight:900;font-size:20px;letter-spacing:1px}
  .years .over{position:absolute;left:72px;top:-8px;width:46px;height:22px;border-radius:23px 23px 0 0;background:var(--silver-1);color:var(--ink);font-size:10px;font-weight:700;text-align:center;line-height:24px}
  .years .tag{position:absolute;left:0;top:42px;width:190px;text-align:center;color:var(--white);font-size:10px;font-weight:700;letter-spacing:.5px}
</style>
</head>
<body>

<section class="card card--front" aria-label="Card front">
  <svg class="card-bg" viewBox="0 0 700 400" preserveAspectRatio="none">
    <defs>
      <linearGradient id="silverBand" x1="0" y1="0" x2="1" y2="0">
        <stop offset="0" stop-color="var(--silver-1)"/>
        <stop offset=".6" stop-color="var(--silver-2)"/>
        <stop offset="1" stop-color="var(--silver-1)"/>
      </linearGradient>
      <linearGradient id="greenBand" x1="0" y1="0" x2="1" y2="0">
        <stop offset="0" stop-color="var(--green-light)"/>
        <stop offset="1" stop-color="var(--green-dark)"/>
      </linearGradient>
    </defs>
    <rect width="700" height="400" fill="var(--card-dark)"/>
    <polygon points="180,0 330,0 150,400 0,400 0,340" fill="var(--card-dark-2)" opacity=".6"/>
    <rect x="0" y="100" width="700" height="120" fill="url(#silverBand)"/>
    <polygon points="450,188 700,188 700,222 430,222" fill="url(#greenBand)"/>
    <polygon points="0,325 280,325 310,368 0,368" fill="url(#greenBand)"/>
    <polygon points="280,325 310,368 700,368 700,400 300,400" fill="url(#silverBand)" opacity=".9"/>
  </svg>

  <div class="abs logo-mark"><span class="square"></span><span class="name">CLEARLINE</span></div>
  <div class="abs title">
    <div class="main">CLEARLINE</div>
    <div class="sub">COMMERCIAL BUILDERS</div>
  </div>
  <p class="abs licenses"><b>LICENSES :</b> &nbsp;» A - General Engineering &nbsp;» B - General Building<br>» C21 Demo/Bldg. Moving &nbsp;» C36 Plumbing</p>
  <p class="abs naics"><b>NAICS CODES:</b> 236220, 238110, 236118, 23810, 238350, 2389390, 327320</p>
  <div class="abs license-tab">LICENSE #1047288</div>
  <p class="abs lbi">LICENSED &nbsp;|&nbsp; BONDED &nbsp;|&nbsp; INSURED</p>
  <svg class="abs seal seal--one" viewBox="0 0 96 96" role="img" aria-label="Certification badge"><circle cx="48" cy="48" r="44" fill="var(--white)"/></svg>
  <svg class="abs seal seal--two" viewBox="0 0 96 96" role="img" aria-label="Certification badge"><circle cx="48" cy="48" r="44" fill="var(--white)"/></svg>
</section>

<section class="card card--back" aria-label="Card back">
  <svg class="card-bg" viewBox="0 0 700 400" preserveAspectRatio="none">
    <defs>
      <linearGradient id="greenSwoosh" x1="0" y1="0" x2="1" y2="0">
        <stop offset="0" stop-color="var(--green-light)"/>
        <stop offset="1" stop-color="var(--green-dark)"/>
      </linearGradient>
    </defs>
    <rect width="700" height="400" fill="var(--card-dark)"/>
    <polygon points="560,0 700,0 700,260" fill="var(--card-dark-2)" opacity=".7"/>
    <path d="M0,0 H360 C330,170 290,320 200,400 H0 Z" fill="url(#greenSwoosh)"/>
    <path d="M0,0 H345 C315,170 270,310 180,400 H0 Z" fill="var(--silver-1)"/>
    <path d="M0,300 C80,330 150,350 230,345 L200,400 H0 Z" fill="url(#greenSwoosh)" opacity=".85"/>
  </svg>

  <div class="abs back-logo"><span class="square"></span><span class="name">CLEARLINE</span></div>
  <div class="abs back-sub">COMMERCIAL BUILDERS</div>
  <div class="abs serving" style="background:linear-gradient(90deg,var(--green-dark),var(--green))">Serving all of Southern California</div>

  <div class="abs person">
    <div class="name">Marcus Hale, DMP</div>
    <div class="role">President, Founder &amp; CEO</div>
  </div>
  <ul class="abs contacts">
    <li><svg viewBox="0 0 24 24"><path d="M6.6 10.8a15 15 0 0 0 6.6 6.6l2.2-2.2a1 1 0 0 1 1-.25 11.4 11.4 0 0 0 3.6.57 1 1 0 0 1 1 1V20a1 1 0 0 1-1 1A17 17 0 0 1 3 4a1 1 0 0 1 1-1h3.5a1 1 0 0 1 1 1c0 1.25.2 2.45.57 3.57a1 1 0 0 1-.25 1z"/></svg>(310) 555-0148</li>
    <li><svg viewBox="0 0 24 24"><path d="M2 5h20v14H2z M2 5l10 8 10-8" fill="none" stroke="var(--green-light)" stroke-width="2"/></svg>marcus@clearlinebuilders.com</li>
    <li><svg viewBox="0 0 24 24"><circle cx="12" cy="12" r="9" fill="none" stroke="var(--green-light)" stroke-width="2"/><path d="M3 12h18M12 3c3 3 3 15 0 18M12 3c-3 3-3 15 0 18" fill="none" stroke="var(--green-light)" stroke-width="1.6"/></svg>www.clearlinebuilders.com</li>
    <li class="license">LICENSE #1047288</li>
  </ul>
  <div class="abs years">
    <div class="over">OVER</div>
    <div class="ribbon">25 YEARS</div>
    <div class="tag">OF SERVICE EXCELLENCE</div>
  </div>
</section>

</body>
</html>
```